Business Card Design

chiropractor. Searching for a fresh cool look. Tired of all the run of the mill designs. I am open tocolors and all new designs..

Target Market(s)

auto accidents workers compensation and private insurance

Industry/Entity Type

Business

Contact Information for Business Card

Dr. Mark S. Snyder193-02 northern blvd.Flushing, new york 11358Upper level rear suitephone 718 224 3605fax 718 555 0187

Font styles to use
Sans Serif

Requirements
Must have
• my office hours on back of card
• Monday 8am-11am; 3pm-6:30pm
• Tuesday 1pm-6pm
• wednesday 9am-noon; 2;30pm-7pm
• Thursday 3pm-8pm
• friday4pm-7pm
Nice to have
• some kind of real cool logo

```html
<!DOCTYPE html>
<html lang="en">
<head>
<meta charset="utf-8">
<title>Chiropractor Business Card</title>
<link rel="stylesheet" href="https://fonts.googleapis.com/css2?family=Arimo:wght@400;700&display=swap">
<style>
  :root {
    --page-bg: #2a2624;
    --front-green: #a8c49b;
    --back-green: #5f7e5d;
    --brand-brown: #6b4728;
    --brand-mark: #8f7a3a;
    --card-text: #ffffff;
    --rule: rgba(255, 255, 255, 0.7);
  }
  html, body {
    margin: 0;
    padding: 0;
    width: 1200px;
    height: 800px;
    overflow: hidden;
    background: var(--page-bg);
    font-family: "Arimo", Arial, sans-serif;
  }
  .canvas {
    position: relative;
    width: 1200px;
    height: 800px;
  }
  .card {
    position: absolute;
    top: 250px;
    width: 520px;
    height: 300px;
    box-sizing: border-box;
  }
  .card-front {
    left: 50px;
    background: var(--front-green);
    display: flex;
    align-items: center;
    justify-content: center;
    gap: 18px;
  }
  .brand-mark {
    width: 74px;
    height: 74px;
    border-radius: 50%;
    background: var(--brand-mark);
  }
  .brand-name {
    color: var(--brand-brown);
    font-size: 44px;
    font-weight: 400;
    letter-spacing: 0.5px;
  }
  .card-back {
    left: 630px;
    background: var(--back-green);
    color: var(--card-text);
  }
  .rule {
    position: absolute;
    height: 1px;
    background: var(--rule);
  }
  .rule-top { top: 92px; left: 235px; right: 22px; }
  .rule-bottom { top: 218px; left: 30px; right: 22px; }
  .doctor-name {
    position: absolute;
    left: 30px;
    top: 104px;
    margin: 0;
    font-size: 22px;
    font-weight: 400;
  }
  .hours {
    position: absolute;
    top: 144px;
    margin: 0;
    padding: 0;
    list-style: none;
    font-size: 12.5px;
    line-height: 20px;
    white-space: nowrap;
  }
  .hours-left { left: 30px; }
  .hours-right { left: 318px; }
  .hours li {
    display: flex;
    align-items: center;
    gap: 6px;
  }
  .leaf { width: 10px; height: 10px; flex: none; }
  .contact {
    position: absolute;
    left: 30px;
    top: 234px;
    margin: 0;
    font-size: 12.5px;
    line-height: 21px;
    font-style: normal;
    white-space: nowrap;
  }
</style>
</head>
<body>
<main class="canvas">
  <section class="card card-front">
    <span class="brand-mark" aria-hidden="true"></span>
    <span class="brand-name">Chiropractor</span>
  </section>

  <section class="card card-back">
    <div class="rule rule-top"></div>
    <h1 class="doctor-name">Dr. Paul T. Wexley</h1>
    <ul class="hours hours-left">
      <li><svg class="leaf" viewBox="0 0 10 10" aria-hidden="true"><path d="M1 9 C1 4 4 1 9 1 C9 6 6 9 1 9 Z" fill="#fff"/></svg>Monday 8am-11am; 3pm-6:30pm</li>
      <li><svg class="leaf" viewBox="0 0 10 10" aria-hidden="true"><path d="M1 9 C1 4 4 1 9 1 C9 6 6 9 1 9 Z" fill="#fff"/></svg>Wednesday 8am-11am; 3pm-6:30pm</li>
      <li><svg class="leaf" viewBox="0 0 10 10" aria-hidden="true"><path d="M1 9 C1 4 4 1 9 1 C9 6 6 9 1 9 Z" fill="#fff"/></svg>Friday 10am-2pm</li>
    </ul>
    <ul class="hours hours-right">
      <li><svg class="leaf" viewBox="0 0 10 10" aria-hidden="true"><path d="M1 9 C1 4 4 1 9 1 C9 6 6 9 1 9 Z" fill="#fff"/></svg>Tuesday 1pm-6pm</li>
      <li><svg class="leaf" viewBox="0 0 10 10" aria-hidden="true"><path d="M1 9 C1 4 4 1 9 1 C9 6 6 9 1 9 Z" fill="#fff"/></svg>Thursday 3pm-8pm</li>
    </ul>
    <div class="rule rule-bottom"></div>
    <address class="contact">
      287-14 Hollis Ridge Rd. Flushing, New York 11472 Second Floor Suite B<br>
      Phone 718 555 0142 &nbsp;Fax 718 555 0187
    </address>
  </section>
</main>
</body>
</html>
```